Webdesign für Coaching von Erwachsenen und Kindern
Zielgruppe
Ich coache Erwachsene und Kinder mit den Methoden des NLP. Meine Zielgruppe sind primär Eltern und auch Lehrer. Mein Ziel sind mehr glückliche Kinder, indem ich primär die Eltern und teilweise auch die Kinder coache.
Mir ist es wichtig souverän und nicht wie eine Kindergärtnerin zu wirken.
Aufgabenstellung
Meine Website: www.coach-merlinger.ch ist mit Wordpress erstellt.
Das Logo besteht bereits und soll so belassen werden. Die Farben des Logos dürfen aufgegriffen werden. Es soll alles zusammenpassen und 'rund' wirken.
Mir gefällt zum Beispiel die Website lumaquo.ch oder Pflegewerk-nord.ch

```html
<!DOCTYPE html>
<html lang="de">
<head>
<meta charset="utf-8">
<title>Lena Merlinger – Coaching</title>
<link href="https://fonts.googleapis.com/css2?family=Allura&family=Montserrat:wght@400;500;600&display=swap" rel="stylesheet">
<style>
  :root {
    --bg: #edf0f5;
    --band: #e1e8f1;
    --navy: #0b3d82;
    --blue: #0a7cc4;
    --ink: #1b1b1f;
    --white: #ffffff;
  }
  * { margin: 0; padding: 0; box-sizing: border-box; }
  html, body { width: 1200px; height: 688px; overflow: hidden; }
  body {
    position: relative;
    background: var(--bg);
    font-family: "Montserrat", Arial, sans-serif;
    color: var(--ink);
  }
  .site-header {
    position: absolute; left: 0; top: 0; width: 1200px; height: 190px;
  }
  .main-nav {
    position: absolute; left: 108px; top: 84px;
    display: flex; gap: 37px;
    font-size: 15px;
  }
  .main-nav a { color: var(--ink); text-decoration: none; padding-bottom: 5px; }
  .main-nav a.active { border-bottom: 3px solid var(--navy); }
  .brand {
    position: absolute; left: 470px; top: 72px; width: 265px;
    display: flex; align-items: center; justify-content: center; gap: 12px;
  }
  .brand-dot {
    width: 14px; height: 14px; border-radius: 50%; background: var(--navy);
  }
  .brand-name {
    font-size: 26px; font-weight: 500; color: var(--navy); white-space: nowrap;
  }
  .header-mail {
    position: absolute; left: 805px; top: 84px;
    display: flex; align-items: center; gap: 8px;
    font-size: 15px; color: var(--ink); text-decoration: none;
  }
  .hero-photo {
    position: absolute; left: 635px; top: 192px; width: 565px; height: 446px;
    background: radial-gradient(ellipse at 55% 50%, #e9d6c8 0%, #f2ece8 45%, #f7f8fa 70%, var(--bg) 100%);
  }
  .hero-text { position: absolute; left: 107px; top: 214px; width: 540px; }
  .hero-title {
    font-family: "Allura", cursive;
    font-weight: 400;
    font-size: 56px; line-height: 59px;
    color: var(--navy);
  }
  .hero-lead {
    margin-top: 24px;
    font-size: 14.5px; line-height: 21px;
  }
  .cta {
    display: inline-block; margin-top: 29px;
    height: 44px; padding: 0 21px; line-height: 41px;
    border-radius: 22px; border: 2px solid var(--navy);
    background: var(--blue); color: var(--white);
    font-size: 15px; font-weight: 500; text-decoration: none;
  }
  .bottom-band {
    position: absolute; left: 0; top: 638px; width: 1200px; height: 50px;
    background: var(--band);
  }
</style>
</head>
<body>
  <header class="site-header">
    <nav class="main-nav">
      <a href="#">Angebote</a>
      <a href="#" class="active">Über Mich</a>
      <a href="#">Kontakt</a>
    </nav>
    <div class="brand">
      <span class="brand-dot"></span>
      <span class="brand-name">Lena Merlinger</span>
    </div>
    <a class="header-mail" href="#">
      <svg width="15" height="12" viewBox="0 0 15 12" aria-hidden="true">
        <rect x="1" y="1" width="13" height="10" rx="1.5" fill="none" stroke="#0b3d82" stroke-width="1.6"/>
        <path d="M1.5 2 L7.5 6.8 L13.5 2" fill="none" stroke="#0b3d82" stroke-width="1.6"/>
      </svg>
      lena@coach-merlinger.ch
    </a>
  </header>

  <div class="hero-photo" role="img" aria-label="Foto: zwei lachende Kinder, die nebeneinander auf verschränkten Armen liegen"></div>

  <section class="hero-text">
    <h1 class="hero-title">Glückliche Kinder durch entspannte Eltern, Lehrerinnen und Lehrer</h1>
    <p class="hero-lead">Ich coache Eltern, Lehrerinnen und Lehrer und Kinder im Einzelsetting und biete Workshops für mehrere Personen an.</p>
    <a class="cta" href="#">ZUM KONTAKFORMULAR</a>
  </section>

  <div class="bottom-band"></div>
</body>
</html>
```